Design the best looking box truck wrap in town for an insulation and whole house fan contractor.

I would like to update my vehicle wrap look for Marlow Power Systems. Our main products are insulation and whole house fans.
I got my car wrapped recently and would like to adopt a similar look to it.

I thought it important to include a picture of my current wrap design and what I don’t like about it so as to show more what I’m looking for.
I’m looking for a more simple design.

Target Market(s)

High End Homeowners

Industry/Entity Type

Marlow power systems

Colors
0054AA
0677BA
7BADD7
CADEEF
E8F1F8
59FF00
82FF00
B8FF75
E3FFCB
F4FFEA

Requirements
Must have
• Logo as the Focal point. Insulation & Whole House fans. 482-316-9027 KRT5830196
Nice to have
• The logo as the focal point that stands out the most.
Should not have
• Pictures. Any services other than insulation and whole house fans

```html
<!DOCTYPE html>
<html lang="en">
<head>
<meta charset="utf-8">
<title>Marlow Power Systems – Box Truck Wrap</title>
<link rel="stylesheet" href="https://fonts.googleapis.com/css2?family=Exo+2:wght@500&family=Anton&family=Montserrat:wght@700;800&family=Satisfy&display=swap">
<style>
  :root {
    --page-bg: #a6a6a6;
    --white: #ffffff;
    --bright-blue: #0a78e6;
    --deep-blue: #2a5db3;
    --logo-blue: #1273e6;
    --lime: #82ff00;
    --halftone: #9a9a9a;
  }
  * { margin: 0; padding: 0; box-sizing: border-box; }
  html, body {
    width: 979px;
    height: 1200px;
    overflow: hidden;
    background: var(--page-bg);
  }
  .wrap-panel {
    position: absolute;
    left: 40px;
    top: 423px;
    width: 900px;
    height: 354px;
    background: var(--white);
    overflow: hidden;
  }
  .wrap-art {
    position: absolute;
    inset: 0;
    width: 100%;
    height: 100%;
  }
  .brand-block {
    position: absolute;
    left: 60px;
    top: 44px;
    width: 400px;
    display: flex;
    flex-direction: column;
    align-items: center;
  }
  .brand-mark {
    width: 96px;
    height: 96px;
    border-radius: 50%;
    background: var(--logo-blue);
  }
  .brand-name {
    margin-top: 28px;
    font-family: "Exo 2", sans-serif;
    font-weight: 500;
    font-size: 36px;
    line-height: 40px;
    letter-spacing: 2px;
    color: var(--logo-blue);
    text-transform: uppercase;
    text-align: center;
  }
  .tagline {
    margin-top: 12px;
    font-family: "Satisfy", cursive;
    font-size: 28px;
    line-height: 1;
    color: var(--logo-blue);
    text-align: center;
  }
  .services {
    position: absolute;
    right: 19px;
    top: 104px;
    text-align: right;
    font-family: "Anton", sans-serif;
    font-weight: 400;
    color: var(--white);
    font-size: 31px;
    line-height: 37px;
    text-transform: uppercase;
    letter-spacing: 0.3px;
  }
  .contact-phone {
    position: absolute;
    right: 19px;
    top: 230px;
    display: flex;
    align-items: center;
    gap: 8px;
    font-family: "Montserrat", sans-serif;
    font-weight: 800;
    font-size: 23px;
    color: var(--white);
  }
  .contact-phone svg { width: 24px; height: 24px; }
  .license {
    position: absolute;
    right: 19px;
    top: 268px;
    font-family: "Montserrat", sans-serif;
    font-weight: 700;
    font-size: 14px;
    color: var(--white);
    letter-spacing: 0.3px;
  }
</style>
</head>
<body>
  <main class="wrap-panel">
    <svg class="wrap-art" viewBox="0 0 900 354" preserveAspectRatio="none" aria-hidden="true">
      <defs>
        <linearGradient id="blueFill" x1="0" y1="0" x2="0" y2="1">
          <stop offset="0" stop-color="#2a5db3"/>
          <stop offset="1" stop-color="#0a78e6"/>
        </linearGradient>
        <linearGradient id="halftoneRight" x1="0" y1="0" x2="1" y2="0">
          <stop offset="0" stop-color="#9a9a9a" stop-opacity="0"/>
          <stop offset="1" stop-color="#9a9a9a" stop-opacity="0.55"/>
        </linearGradient>
        <linearGradient id="halftoneLeft" x1="1" y1="0" x2="0" y2="0">
          <stop offset="0" stop-color="#9a9a9a" stop-opacity="0"/>
          <stop offset="1" stop-color="#9a9a9a" stop-opacity="0.5"/>
        </linearGradient>
      </defs>
      <path role="img" aria-label="grey halftone dot texture" fill="url(#halftoneLeft)" d="M0,200 C25,110 100,40 215,0 H150 C90,25 30,80 0,145 Z"/>
      <path fill="url(#blueFill)" d="M0,0 H150 C90,25 30,80 0,145 Z"/>
      <path fill="var(--lime)" d="M0,138 C30,78 85,28 140,0 H122 C72,30 28,75 0,118 Z"/>
      <path role="img" aria-label="grey halftone dot texture" fill="url(#halftoneRight)" d="M560,0 H636 C616,150 540,270 415,338 C500,260 560,150 560,0 Z"/>
      <path fill="url(#blueFill)" d="M675,0 H900 V354 H386 C520,300 640,170 675,0 Z"/>
      <path fill="var(--lime)" d="M636,0 H675 C645,160 540,295 400,348 C525,280 615,160 636,0 Z"/>
    </svg>

    <div class="brand-block">
      <div class="brand-mark"></div>
      <h1 class="brand-name">Marlow Power<br>Systems</h1>
      <p class="tagline">Comfort You Can Count On</p>
    </div>

    <h2 class="services">Insulation &amp;<br>Whole House Fans</h2>
    <p class="contact-phone">
      <svg viewBox="0 0 24 24" aria-hidden="true">
        <circle cx="12" cy="12" r="12" fill="#ffffff"/>
        <path fill="#1a6fd6" d="M8.6 6.2c.4-.3.9-.2 1.1.2l1.2 2.1c.2.4.1.8-.2 1.1l-.8.7c.6 1.3 1.6 2.4 2.9 3.1l.7-.8c.3-.3.8-.4 1.1-.2l2.1 1.2c.4.2.5.7.2 1.1l-.9 1.2c-.4.5-1 .7-1.6.5-3.3-1.1-5.8-3.6-6.8-6.9-.2-.6 0-1.2.5-1.600z"/>
      </svg>
      482-316-9027
    </p>
    <p class="license">KRT5830196</p>
  </main>
</body>
</html>
```